Runlark

I have a web site RUNLARK.com that is in serious need of a re-design. The site is mean't to be a portal for an app that I have called RUNLARK which you can see in the plain badge or googleplay. Take a look and see what you can do.
Updates

Project Deadline Extended
Reason: Still working with designers. The "look" is not quite there but a lot of progress has been made. MB

Industry/Entity Type

Store

```html
<!DOCTYPE html>
<html lang="en">
<head>
<meta charset="utf-8">
<title>Runlark</title>
<link href="https://fonts.googleapis.com/css2?family=Open+Sans:wght@400;600;700;800&display=swap" rel="stylesheet">
<style>
:root{
  --blue:#1c6db4;
  --blue-dark:#12508a;
  --ink:#222;
  --muted:#666;
  --dark:#1f2226;
  --panel:#ffffff;
  --gray:#e6e7e9;
  --line:#cfd2d6;
}
*{box-sizing:border-box;margin:0;padding:0}
html,body{width:865px;height:1200px;overflow:hidden}
body{font-family:"Open Sans",Arial,sans-serif;color:var(--ink);background:#fff;position:relative}
.abs{position:absolute}

.topbar{left:0;top:0;width:865px;height:20px;background:#f1f2f3;border-bottom:1px solid #ddd}
.social{top:4px;width:12px;height:12px;background:var(--blue);border-radius:2px}
.toplinks{right:78px;top:3px;font-size:8px;font-weight:700;color:#555;letter-spacing:.5px}

.header{left:0;top:20px;width:865px;height:95px;background:#fff}
.logo{left:78px;top:24px;display:flex;align-items:center;gap:8px;font-size:30px;font-weight:800;color:var(--blue);letter-spacing:-.5px}
.logo-dot{width:22px;height:22px;border-radius:50%;background:var(--blue)}
.nav{right:77px;top:30px;display:flex;font-size:10px;font-weight:700}
.nav a{padding:10px 11px;color:#333;text-decoration:none}
.nav a.active{color:var(--blue);border-bottom:3px solid var(--blue)}

.hero{left:0;top:115px;width:865px;height:655px;background:linear-gradient(180deg,#262a30 0%,#3a3f46 55%,#5c4a3e 80%,#2b2e33 100%)}
.slide{left:78px;top:130px;width:710px;height:305px;background:linear-gradient(135deg,#6b4a32 0%,#a4703f 40%,#3b3f49 75%,#1e2127 100%)}
.caption{left:78px;top:350px;width:710px;height:85px;background:rgba(0,0,0,.6);padding:14px 18px}
.caption h2{font-size:15px;color:#fff;font-weight:600}
.caption p{font-size:8px;color:#ccc;margin-top:6px}
.arrow{width:26px;height:26px;border-radius:50%;background:rgba(0,0,0,.55);border:1px solid #888;display:flex;align-items:center;justify-content:center}

.tabs{left:78px;top:435px;width:710px;height:80px;background:#16191d;display:flex}
.tab{flex:1;display:flex}
.tab-label{width:50%;padding:14px 10px;color:#fff;font-size:12px;font-weight:700}
.tab-label span{display:block;font-size:7px;font-weight:400;color:#ccc;margin-top:5px}
.tab.on .tab-label{background:var(--blue)}
.tab-thumb{width:50%;background:linear-gradient(135deg,#5e6876,#2a2f36)}

.card{top:540px;width:222px;height:215px;background:var(--panel);border-top:3px solid var(--blue)}
.card-head{height:30px;display:flex;align-items:center;justify-content:space-between;padding:0 10px;font-size:10px;font-weight:800;color:#333}
.dots{letter-spacing:2px;color:#999;font-size:8px}
.card-body{position:absolute;left:6px;right:6px;top:33px;bottom:6px}
.result{background:linear-gradient(#4a4f57,#262a30);color:#fff;text-align:center;padding-top:14px}
.result h3{font-size:14px;font-weight:700}
.score-row{display:flex;justify-content:center;align-items:center;gap:14px;margin-top:22px}
.crest{width:40px;height:40px;border-radius:50%;background:#c9ccd1}
.score{background:#fff;color:#222;font-size:22px;font-weight:800;padding:2px 10px}
.teams{display:flex;justify-content:space-between;font-size:8px;margin:12px 34px 0}
.date{font-size:8px;color:#ccc;margin-top:14px}
.player{background:linear-gradient(160deg,#8aa0b8,#324a6e 70%,#7a1d2c)}
.player .tag{position:absolute;left:0;right:0;bottom:0;background:rgba(0,0,0,.6);color:#fff;font-size:9px;padding:5px 8px}
.live{background:linear-gradient(150deg,#5a6b3a,#2c3a22 60%,#1c2414)}
.play{position:absolute;left:86px;top:62px;width:40px;height:40px;border-radius:50%;background:rgba(255,255,255,.8)}

.lower{left:0;top:770px;width:865px;height:300px;background:var(--gray)}
.box{background:#fff;border:1px solid var(--line)}
.tabhead{display:flex;font-size:9px;font-weight:800}
.tabhead div{flex:1;padding:7px 0;text-align:center}
.tabhead .on{background:var(--blue);color:#fff}
.tabhead .off{background:#dfe1e4;color:#444}
.item{display:flex;gap:8px;padding:8px;border-bottom:1px solid #e3e3e3}
.thumb{width:36px;height:36px;flex:none;background:linear-gradient(135deg,#8b8f96,#3c4048)}
.item b{display:block;font-size:8px;color:#333}
.item span{display:block;font-size:7px;color:var(--muted);line-height:1.4;margin-top:2px}
.mid h4{font-size:10px;font-weight:800;color:#333}
.mid p{font-size:8.5px;color:#555;line-height:1.6;margin-top:8px}
.sponsor-title{font-size:10px;font-weight:800;color:#333;text-align:center;margin-top:24px;border-top:1px solid var(--line);padding-top:10px}
.sponsors{display:flex;justify-content:center;gap:14px;margin-top:14px}
.sponsor{width:34px;height:34px;border-radius:50%;background:#b9bec6}
.righthead{background:var(--blue-dark);color:#fff;font-size:9px;font-weight:800;padding:7px 10px}

.apps-title{left:78px;top:1088px;font-size:11px;font-weight:800;color:#333}
.badge{top:1110px;width:96px;height:30px;background:#111;border-radius:5px}
.sub-title{left:560px;top:1088px;font-size:11px;font-weight:800;color:#333}
.sub-input{left:560px;top:1112px;width:200px;height:26px;border:1px solid var(--line);font-size:8px;color:#999;padding:7px 8px}
.sub-btn{left:760px;top:1112px;width:28px;height:26px;background:var(--blue);display:flex;align-items:center;justify-content:center}

.footer{left:0;top:1160px;width:865px;height:40px;background:#eceded;border-top:1px solid #ddd;font-size:8px;color:#666}
.footer .links{position:absolute;left:78px;top:15px}
.footer .copy{position:absolute;right:77px;top:15px}
</style>
</head>
<body>

<div class="abs topbar">
  <div class="abs social" style="left:78px"></div>
  <div class="abs social" style="left:94px"></div>
  <div class="abs toplinks">FAQ &nbsp;|&nbsp; CONTACT US</div>
</div>

<header class="abs header">
  <div class="abs logo"><span class="logo-dot"></span>Runlark</div>
  <nav class="abs nav">
    <a class="active">HOME</a><a>ABOUT US</a><a>EVENTS</a><a>PHOTOS</a><a>LIVE SCORE</a><a>SPORTS NEWS</a>
  </nav>
</header>

<section class="abs hero" role="img" aria-label="Blurred stadium crowd background"></section>

<div class="abs slide" role="img" aria-label="Basketball players jumping for the ball"></div>
<div class="abs caption">
  <h2>Lorem ipsum dolor sit amet consectetur adipiscing elit</h2>
  <p>Proin viverra augue purus, eu cursus nibh vestibulum quis. Nunc non velit nisi vestibulum quis.</p>
</div>
<div class="abs arrow" style="left:64px;top:270px"><svg width="10" height="10" viewBox="0 0 10 10"><path d="M7 1L3 5l4 4" stroke="#fff" stroke-width="2" fill="none"/></svg></div>
<div class="abs arrow" style="left:775px;top:270px"><svg width="10" height="10" viewBox="0 0 10 10"><path d="M3 1l4 4-4 4" stroke="#fff" stroke-width="2" fill="none"/></svg></div>

<div class="abs tabs">
  <div class="tab on"><div class="tab-label">Basketball<span>Lorem ipsum dolor sit amet consectetur</span></div><div class="tab-thumb" role="img" aria-label="Basketball thumbnail"></div></div>
  <div class="tab"><div class="tab-label">Hockey<span>Lorem ipsum dolor sit amet consectetur</span></div><div class="tab-thumb" role="img" aria-label="Hockey thumbnail"></div></div>
  <div class="tab"><div class="tab-label">Baseball<span>Lorem ipsum dolor sit amet consectetur</span></div><div class="tab-thumb" role="img" aria-label="Baseball thumbnail"></div></div>
</div>

<div class="abs arrow" style="left:78px;top:635px;width:20px;height:20px;background:#fff;border:none"><svg width="8" height="8" viewBox="0 0 10 10"><path d="M7 1L3 5l4 4" stroke="#333" stroke-width="2" fill="none"/></svg></div>
<div class="abs arrow" style="left:768px;top:635px;width:20px;height:20px;background:#fff;border:none"><svg width="8" height="8" viewBox="0 0 10 10"><path d="M3 1l4 4-4 4" stroke="#333" stroke-width="2" fill="none"/></svg></div>

<div class="abs card" style="left:105px">
  <div class="card-head">RECENT RESULTS<span class="dots">●●●●●●</span></div>
  <div class="card-body result">
    <h3>Liga Nova</h3>
    <div class="score-row"><div class="crest"></div><div class="score">2 - 2</div><div class="crest"></div></div>
    <div class="teams"><span>Home</span><span>Away</span></div>
    <div class="date">Sat, 12 Oct 2013</div>
  </div>
</div>
<div class="abs card" style="left:322px">
  <div class="card-head">PLAYERS<span class="dots">●●●●●●</span></div>
  <div class="card-body player" role="img" aria-label="Football player in action">
    <div class="tag">Leon Varro Football</div>
  </div>
</div>
<div class="abs card" style="left:539px">
  <div class="card-head">LIVE MATCH<span class="dots">●●●●●●</span></div>
  <div class="card-body live" role="img" aria-label="Live match video still">
    <div class="play"><svg width="40" height="40" viewBox="0 0 40 40"><path d="M16 12l12 8-12 8z" fill="#333"/></svg></div>
  </div>
</div>

<section class="abs lower"></section>

<div class="abs box" style="left:78px;top:785px;width:222px;height:270px">
  <div class="tabhead"><div class="off">POPULAR</div><div class="on">LATEST</div></div>
  <div class="item"><div class="thumb"></div><div><b>Lorem ipsum dolor sit</b><span>Proin viverra augue purus eu cursus nibh quis</span></div></div>
  <div class="item"><div class="thumb"></div><div><b>Lorem ipsum dolor sit</b><span>Proin viverra augue purus eu cursus nibh quis</span></div></div>
  <div class="item"><div class="thumb"></div><div><b>Lorem ipsum dolor sit</b><span>Proin viverra augue purus eu cursus nibh quis</span></div></div>
  <div class="item" style="border:none"><div class="thumb"></div><div><b>Lorem ipsum dolor sit</b><span>Proin viverra augue purus eu cursus nibh quis</span></div></div>
</div>

<div class="abs mid" style="left:318px;top:792px;width:225px">
  <h4>SPORT STATS ON DEMAND</h4>
  <p>Forget about relying on sportscasters or the banner moving on the bottom of your screen for the scores you want. Just select your league, go to team data, go to the game you're interested in and get the score. All in a matter of seconds.</p>
  <div class="sponsor-title">OUR SPONSORS</div>
  <div class="sponsors"><div class="sponsor"></div><div class="sponsor"></div><div class="sponsor"></div><div class="sponsor"></div></div>
</div>

<div class="abs box" style="left:563px;top:785px;width:225px;height:270px">
  <div class="righthead">PAST TEAM PERFORMANCE</div>
  <div class="item"><div class="thumb"></div><div><b>Calder</b><span>Lorem ipsum dolor sit amet consectetur elit</span></div></div>
  <div class="item"><div class="thumb"></div><div><b>Lorem ipsum dolor</b><span>Lorem ipsum dolor sit amet consectetur elit</span></div></div>
  <div class="item"><div class="thumb"></div><div><b>Lorem ipsum dolor</b><span>Lorem ipsum dolor sit amet consectetur elit</span></div></div>
  <div class="item" style="border:none"><div class="thumb"></div><div><b>Lorem ipsum dolor</b><span>Lorem ipsum dolor sit amet consectetur elit</span></div></div>
</div>

<div class="abs apps-title">RUNLARK MOBILE APPS ARE HERE</div>
<div class="abs badge" style="left:78px"></div>
<div class="abs badge" style="left:184px"></div>

<div class="abs sub-title">SUBSCRIBE WITH US</div>
<div class="abs sub-input">Enter your email...</div>
<div class="abs sub-btn"><svg width="10" height="10" viewBox="0 0 10 10"><path d="M3 1l4 4-4 4" stroke="#fff" stroke-width="2" fill="none"/></svg></div>

<footer class="abs footer">
  <div class="links">Home &nbsp;/&nbsp; About Us &nbsp;/&nbsp; Events &nbsp;/&nbsp; Live Scores &nbsp;/&nbsp; News &nbsp;/&nbsp; Sports &nbsp;/&nbsp; Photos &nbsp;/&nbsp; Faqs &nbsp;/&nbsp; Contact Us</div>
  <div class="copy">© 2014 Runlark. All right reserved</div>
</footer>

</body>
</html>
```